Business Card for a Jewellery Brand

Business card for an upscale jewellery brand. Attached is the brand logo and icon and color board. I am looking for two card versions: one for the founder and one is generic. The card should be elegant and convey upscale and premium feel. I am open to both square and rectangle card shapes.

Industry/Entity Type

Jewelry

Contact Information for Business Card

Two cards: (1) Sunila Perumbadi (Founder) (2) General
(1) Sunila Perumbadi card should have Name: Sunila Perumbadi, Title: Founder Email id: sunila@quelm.com.au. Phone no: +61412555307
(2) Generic card should have Email id: info@quelm.com.au. Phone no: +61431555962

Requirements
Must have
• Workmark
• ICON
• Phone no
• Email ID
• ABN: 48917205563 (Note: ABN is Business number in Australia)
• Website: www.quelm.com.au
• Instagram: quelm_jewellery
• Facebook: @quelmjewellery
Nice to have
• Tagline

```html
<!DOCTYPE html>
<html lang="en">
<head>
<meta charset="utf-8">
<title>QUELM — Founder Business Card</title>
<link rel="stylesheet" href="https://fonts.googleapis.com/css2?family=Oswald:wght@600&family=Roboto:wght@500&family=Questrial&family=Josefin+Sans:wght@300&display=swap">
<style>
  :root {
    --rose-deep: #d6848b;
    --rose-mid: #e59a94;
    --rose-blush: #fce4e0;
    --rose-text: #da8189;
    --ink: #111111;
    --ink-soft: #333333;
    --marble-light: #ffffff;
    --marble-vein: #ececec;
  }
  html, body {
    margin: 0;
    padding: 0;
    overflow: hidden;
    background: #f4f4f4;
  }
  .card {
    position: relative;
    width: 1200px;
    height: 686px;
    overflow: hidden;
    background:
      radial-gradient(ellipse at 30% 40%, var(--marble-light) 0%, transparent 60%),
      linear-gradient(135deg, var(--marble-light) 0%, var(--marble-vein) 35%, var(--marble-light) 55%, var(--marble-vein) 80%, var(--marble-light) 100%);
  }
  .card__waves {
    position: absolute;
    inset: 0;
    width: 1200px;
    height: 686px;
  }
  .brand {
    position: absolute;
    left: 468px;
    top: 62px;
    display: flex;
    align-items: center;
    gap: 22px;
  }
  .brand__mark {
    width: 44px;
    height: 44px;
    border-radius: 50%;
    background: var(--rose-mid);
  }
  .brand__name {
    font-family: "Josefin Sans", sans-serif;
    font-weight: 300;
    font-size: 52px;
    letter-spacing: 18px;
    color: var(--rose-mid);
    line-height: 1;
    padding-top: 8px;
  }
  .person {
    position: absolute;
    left: 214px;
    top: 196px;
  }
  .person__name {
    margin: 0;
    font-family: "Oswald", sans-serif;
    font-weight: 600;
    font-size: 54px;
    line-height: 1;
    letter-spacing: 1px;
    color: var(--rose-text);
  }
  .person__title {
    margin: 38px 0 0;
    font-family: "Roboto", sans-serif;
    font-weight: 500;
    font-size: 35px;
    line-height: 1;
    color: var(--ink);
  }
  .contact {
    list-style: none;
    margin: 44px 0 0;
    padding: 0;
  }
  .contact__item {
    display: flex;
    align-items: center;
    height: 40px;
    margin-bottom: 38px;
    font-family: "Questrial", sans-serif;
    font-size: 32px;
    color: var(--ink-soft);
  }
  .contact__icon {
    width: 38px;
    height: 38px;
    margin-right: 22px;
    flex: none;
  }
</style>
</head>
<body>
  <main class="card">
    <svg class="card__waves" viewBox="0 0 1200 686" aria-hidden="true">
      <path d="M0,0 H404 C200,90 40,300 0,560 Z" fill="var(--rose-blush)"/>
      <path d="M0,0 H396 C180,70 40,220 0,425 Z" fill="var(--rose-mid)"/>
      <path d="M1200,0 C1160,300 1000,560 460,686 H1200 Z" fill="var(--rose-mid)"/>
      <path d="M1200,130 C1130,400 950,600 630,686 H1200 Z" fill="var(--rose-deep)"/>
    </svg>

    <div class="brand">
      <span class="brand__mark"></span>
      <span class="brand__name">QUELM</span>
    </div>

    <section class="person">
      <h1 class="person__name">Sunila Perumbadi</h1>
      <p class="person__title">Founder</p>
      <ul class="contact">
        <li class="contact__item">
          <svg class="contact__icon" viewBox="0 0 38 38" aria-hidden="true">
            <rect x="2" y="8" width="34" height="24" fill="none" stroke="var(--ink-soft)" stroke-width="2"/>
            <path d="M2,8 L19,22 L36,8 M2,32 L15,19 M36,32 L23,19" fill="none" stroke="var(--ink-soft)" stroke-width="2"/>
          </svg>
          <span>sunila@quelm.com.au</span>
        </li>
        <li class="contact__item">
          <svg class="contact__icon" viewBox="0 0 24 24" aria-hidden="true">
            <path d="M6.6 10.8c1.4 2.8 3.8 5.1 6.6 6.6l2.2-2.2c.3-.3.7-.4 1-.2 1.1.4 2.3.6 3.6.6.6 0 1 .4 1 1V20c0 .6-.4 1-1 1C10.6 21 3 13.4 3 4c0-.6.4-1 1-1h3.5c.6 0 1 .4 1 1 0 1.3.2 2.5.6 3.6.1.3 0 .7-.2 1z" fill="var(--ink)"/>
          </svg>
          <span>+61412555307</span>
        </li>
      </ul>
    </section>
  </main>
</body>
</html>
```